Newsletter Ad

I am looking for someone to design an advertisement for a mother's club newsletter. 4" wide X by 5" tall (and 2.5" wide X 5" tall if possible).

I'm a psychotherapist, so want the ad to look professional, but modern. I have a logo with my photo attached that can be incorporated into the design. The colors of my website are turquoise and white. I'd like to keep with that theme...so maybe some turquoise blocking to match the logo font color.

I'm uploading a logo as well as an ad draft with the content I'd like listed in the ad.

```html
<!DOCTYPE html>
<html lang="en">
<head>
<meta charset="utf-8">
<title>Dana Merrow, MA, MFT — Newsletter Ad</title>
<link rel="stylesheet" href="https://fonts.googleapis.com/css2?family=Questrial&family=Nunito+Sans:wght@700;800&display=swap">
<style>
  :root {
    --teal-ink: #2f918d;
    --teal-panel: rgba(52, 150, 146, 0.88);
    --water-light: #cfeee6;
    --water-mid: #8fd3cb;
    --water-deep: #4fb3b0;
    --veil: rgba(255, 255, 255, 0.86);
    --veil-soft: rgba(255, 255, 255, 0.72);
    --white: #ffffff;
    --portrait-dark: #1d1a18;
    --portrait-warm: #8a6a4c;
  }
  * { box-sizing: border-box; margin: 0; padding: 0; }
  html, body { width: 960px; height: 1200px; overflow: hidden; background: var(--white); }
  .ad {
    position: relative;
    width: 960px;
    height: 1200px;
    overflow: hidden;
    font-family: "Questrial", "Century Gothic", sans-serif;
  }
  .ad__water {
    position: absolute;
    inset: 0;
    background:
      linear-gradient(180deg, var(--water-light) 0%, var(--water-mid) 45%, var(--water-deep) 80%, var(--water-mid) 100%);
  }
  .ad__header {
    position: absolute;
    left: 36px; top: 36px;
    width: 886px; height: 119px;
    background: var(--veil);
    display: flex;
    align-items: center;
    padding-left: 26px;
  }
  .ad__name {
    color: var(--teal-ink);
    font-weight: 400;
    font-size: 47px;
    letter-spacing: 1px;
  }
  .ad__portrait {
    position: absolute;
    left: 36px; top: 192px;
    width: 390px; height: 586px;
    background: radial-gradient(ellipse at 45% 40%, var(--portrait-warm) 0%, #5b4632 40%, var(--portrait-dark) 80%);
  }
  .ad__contact {
    position: absolute;
    left: 36px; top: 815px;
    width: 392px; height: 347px;
    background: var(--veil-soft);
    color: var(--teal-ink);
    padding: 22px 0 0 22px;
  }
  .ad__contact p { font-size: 29px; line-height: 40px; }
  .ad__contact .ad__web { font-family: "Nunito Sans", sans-serif; font-weight: 700; font-size: 33px; line-height: 50px; }
  .ad__contact .ad__phone { font-family: "Nunito Sans", sans-serif; font-weight: 700; font-size: 37px; line-height: 46px; }
  .ad__contact .ad__license { margin-top: 50px; font-size: 28px; }
  .ad__services {
    position: absolute;
    left: 532px; top: 192px;
    width: 390px; height: 970px;
    background: var(--teal-panel);
    color: var(--white);
    text-align: right;
    padding: 14px 16px 0 0;
  }
  .ad__headline {
    font-family: "Nunito Sans", sans-serif;
    font-weight: 800;
    font-size: 36px;
    line-height: 48px;
  }
  .ad__rule {
    margin: 18px 0 0 22px;
    border-top: 2px dotted rgba(255, 255, 255, 0.6);
    width: 345px;
  }
  .ad__list { list-style: none; margin-top: 54px; }
  .ad__list li { font-size: 31px; line-height: 42px; margin-bottom: 41px; }
  .ad__list li:last-child { margin-bottom: 0; }
</style>
</head>
<body>
<div class="ad">
  <div class="ad__water" role="img" aria-label="Rippling turquoise water surface background"></div>

  <header class="ad__header">
    <h1 class="ad__name">DANA MERROW,MA, MFT</h1>
  </header>

  <div class="ad__portrait" role="img" aria-label="Portrait photo of the therapist"></div>

  <section class="ad__contact">
    <p>418 Harbor Lane</p>
    <p>Cove Point, CA 90000</p>
    <p class="ad__web">www.danamerrow.com</p>
    <p>dana@danamerrow.com</p>
    <p class="ad__phone">555.014.2290</p>
    <p class="ad__license">License# MFC00000</p>
  </section>

  <section class="ad__services">
    <h2 class="ad__headline">Psychotherapy for<br>Individuals<br>Couples<br>and Families</h2>
    <div class="ad__rule"></div>
    <ul class="ad__list">
      <li>Parenting</li>
      <li>Depression</li>
      <li>Anxiety</li>
      <li>Life Transitions</li>
      <li>Divorce</li>
      <li>Couples Issues</li>
      <li>Women's Issues</li>
      <li>Attachment<br>and Neuroscience</li>
    </ul>
  </section>
</div>
</body>
</html>
```